Cellular Reward Program Flyer

We are launching a Customer Reward Program for our cellular retail business…. The marketing piece will be placed on our counter tops on high gloss cardstock or cardboard stand up type signs. I’m trying to keep this as clean and simple as possible. I found a few example’s of what I’d like to use as a basis.
Our biggest feature to our plan is our customers earn $20 every $100 spent. (requires 3 separate purchases)
No cards, no coupons, nothing needed.

our company logo is attached. you can also go to www.vontrelix.com for other info on the company as we are a franchise

Industry/Entity Type

Marketing

```html
<!DOCTYPE html>
<html lang="en">
<head>
<meta charset="utf-8">
<title>Customer Reward Program Flyer</title>
<link rel="stylesheet" href="https://fonts.googleapis.com/css2?family=Roboto+Slab:wght@400;700;800&family=Open+Sans:wght@400;600&display=swap">
<style>
  :root {
    --stage: #1c1c1c;
    --paper: #ffffff;
    --orange-deep: #ffa62b;
    --orange-soft: #ffc25a;
    --ink: #111111;
    --accent: #f7931e;
    --gold: #f6cf1d;
    --muted: #8a8a8a;
    --screen-red: #c8401a;
    --screen-dark: #3a1c12;
    --screen-green: #5e9e2c;
    --frame: #2a2a2a;
  }
  * { margin: 0; padding: 0; box-sizing: border-box; }
  html, body { width: 1200px; height: 1000px; overflow: hidden; background: var(--stage); }
  .flyer {
    position: absolute; left: 280px; top: 105px; width: 636px; height: 823px;
    background: linear-gradient(180deg, var(--orange-deep) 0%, var(--orange-soft) 28%, #ffe3ad 55%, var(--paper) 78%);
    font-family: "Roboto Slab", serif; color: var(--ink); text-align: center;
  }
  .title { position: absolute; top: 50px; left: 0; width: 100%; }
  .title-top { font-size: 28px; font-weight: 400; line-height: 1; letter-spacing: 0.5px; }
  .title-main {
    display: inline-block; margin-top: 2px; padding: 3px 4px 4px;
    font-size: 35px; font-weight: 800; line-height: 1;
    border-top: 1px dashed rgba(0,0,0,0.35); border-bottom: 1px dashed rgba(0,0,0,0.35);
  }
  .devices {
    position: absolute; left: 65px; top: 170px; width: 495px; height: 440px;
  }
  .device-art { position: absolute; inset: 0; }
  .side-label {
    position: absolute; top: 250px; width: 120px; color: #fff;
    font-family: "Open Sans", sans-serif; font-weight: 600; font-size: 40px;
  }
  .side-label.left { left: 10px; }
  .side-label.right { left: 355px; }
  .offer {
    position: absolute; left: 175px; top: 75px; width: 145px;
    color: #fff; line-height: 1;
  }
  .offer span { display: block; padding: 4px 0; border-bottom: 1px dashed rgba(255,255,255,0.35); }
  .offer span:last-child { border-bottom: none; }
  .offer .word { font-size: 44px; font-weight: 400; }
  .offer .amount { font-size: 62px; font-weight: 400; color: var(--gold); }
  .benefit { position: absolute; top: 642px; left: 0; width: 100%; }
  .benefit-heading { font-size: 14px; font-weight: 800; color: var(--accent); letter-spacing: 0.5px; }
  .benefit-body {
    margin: 4px auto 0; width: 420px; font-family: "Open Sans", sans-serif;
    font-size: 11px; line-height: 19px; color: var(--muted);
  }
  .brand {
    position: absolute; top: 760px; left: 0; width: 100%;
    display: flex; justify-content: center; align-items: center; gap: 6px;
  }
  .brand-dot { width: 26px; height: 26px; border-radius: 50%; background: var(--accent); }
  .brand-name { font-family: "Roboto Slab", serif; font-size: 26px; font-weight: 400; color: #333; }
</style>
</head>
<body>
  <main class="flyer">
    <header class="title">
      <div class="title-top">CUSTOMER</div>
      <div class="title-main">REWARD PROGRAM</div>
    </header>

    <section class="devices">
      <svg class="device-art" width="495" height="440" viewBox="0 0 495 440" role="img" aria-label="Three smartphones side by side, a red phone with a shopping basket icon, a black phone in front, and a purple phone with a wallet icon">
        <defs>
          <linearGradient id="screenLeft" x1="0" y1="0" x2="0" y2="1">
            <stop offset="0" stop-color="#e0652a"/><stop offset="1" stop-color="#7a2410"/>
          </linearGradient>
          <linearGradient id="screenRight" x1="0" y1="0" x2="0" y2="1">
            <stop offset="0" stop-color="#9ccc60"/><stop offset="1" stop-color="#3f7c1c"/>
          </linearGradient>
          <linearGradient id="screenCenter" x1="0" y1="0" x2="0" y2="1">
            <stop offset="0" stop-color="#5a2d1a"/><stop offset="1" stop-color="#2a120a"/>
          </linearGradient>
        </defs>
        <rect x="0" y="30" width="180" height="380" rx="30" fill="#e8341a"/>
        <rect x="18" y="80" width="150" height="272" fill="url(#screenLeft)"/>
        <rect x="315" y="30" width="180" height="380" rx="30" fill="#8e1f56"/>
        <rect x="330" y="88" width="148" height="266" fill="url(#screenRight)"/>
        <rect x="135" y="0" width="230" height="440" rx="32" fill="var(--frame)"/>
        <rect x="152" y="55" width="196" height="335" fill="url(#screenCenter)"/>
      </svg>
      <div class="side-label left">$$$</div>
      <div class="side-label right">$$$</div>
      <div class="offer">
        <span class="word">EARN</span>
        <span class="amount">$20</span>
        <span class="word">EVERY</span>
        <span class="amount">$100</span>
        <span class="word">SPENT</span>
      </div>
    </section>

    <section class="benefit">
      <h2 class="benefit-heading">OTHER BENEFIT</h2>
      <p class="benefit-body">to the customer signing up is they never need to keep a receipt for warranty or returns and they are kept up to date on the latest cellular products.</p>
    </section>

    <footer class="brand">
      <span class="brand-dot"></span>
      <span class="brand-name">Vontrelix</span>
    </footer>
  </main>
</body>
</html>
```